Bluegate Physiotherapy
Business Cards, Stationary, Letterhead, Magnet, Presentation Folder, A5 Referral Pad, Email Signatur
Bluegate Physiotherapy -
Creative Brief
Professional
Tom Ellingsworth
BSc Physiotherapy / Acupuncturist / Cert IV Occupational Health & Safety
Unit 3, 48 Kestrel Lane, Pelican Bay WA 6990
tom.ellingsworth@bluegatephysio-example.com.au
www.bluegatephysio-example.com.au
Magnet to be standard business card size (portrait OR landscape) and include only phone, address and website (in addition to graphic component). Referral pad to be A5 size. At the TOP: "Patient Name", "Date" as well as 4 tick boxes "W.C.", "Vet. Affairs", "Private" "EPC". At the BOTTOM: "Referring Doctor" "Sign" "Doctors Name" and "Address" as well as "Preferred Contact" with 4 tick boxes "E-mail", "Phone", "Fax", "Snail Mail". Down one SIDE to have a list: "Manual Therapy", "Massage", "Exercise Prescription", "Gym Based Rehab", "Workplace Assessment", "Ergonomics", "Acupuncture", "Sports Physiotherapy", "Womens Health".

```html
<!DOCTYPE html>
<html lang="en">
<head>
<meta charset="utf-8">
<title>Bluegate Physiotherapy – Stationery Suite</title>
<link href="https://fonts.googleapis.com/css2?family=Open+Sans:wght@400;600;700&display=swap" rel="stylesheet">
<style>
  :root {
    --page: #ffffff;
    --ink: #333333;
    --brand: #1f4f9a;
    --gold-light: #f8d65a;
    --gold: #f0b52a;
    --gold-deep: #e39a17;
    --sky: #cfe6f3;
    --line: #555555;
  }
  * { box-sizing: border-box; margin: 0; padding: 0; }
  html, body { width: 1200px; height: 868px; overflow: hidden; background: var(--page); }
  body { font-family: "Open Sans", Arial, sans-serif; color: var(--ink); position: relative; }

  .gradients { position: absolute; width: 0; height: 0; }

  .piece { position: absolute; background: #fff; box-shadow: 0 1px 4px rgba(0,0,0,.25); overflow: hidden; }
  .piece > svg.art { position: absolute; inset: 0; width: 100%; height: 100%; }

  .brand { position: absolute; display: flex; align-items: center; gap: 8px; color: var(--brand); font-weight: 700; line-height: 1.05; white-space: nowrap; }
  .brand .dot { flex: none; border-radius: 50%; background: var(--gold); }
  .brand--lg { font-size: 34px; gap: 14px; }
  .brand--lg .dot { width: 40px; height: 40px; }
  .brand--md { font-size: 17px; }
  .brand--md .dot { width: 20px; height: 20px; }
  .brand--sm { font-size: 11px; gap: 5px; }
  .brand--sm .dot { width: 12px; height: 12px; }

  .small { position: absolute; font-size: 6.5px; color: var(--ink); line-height: 1.4; white-space: nowrap; }

  .card-back { left: 43px; top: 12px; width: 317px; height: 161px; }
  .card-front { left: 396px; top: 7px; width: 320px; height: 166px; }
  .card-front .name { position: absolute; right: 14px; top: 10px; font-size: 16px; font-weight: 700; color: var(--brand); white-space: nowrap; }
  .card-front .title { position: absolute; right: 14px; top: 33px; text-align: right; font-size: 6.5px; line-height: 1.35; white-space: nowrap; }
  .magnet { left: 536px; top: 134px; width: 274px; height: 146px; transform: rotate(5deg); background: var(--sky); }
  .folder { left: 12px; top: 307px; width: 377px; height: 557px; }
  .letterhead { left: 804px; top: 312px; width: 372px; height: 372px; }
  .envelope { left: 804px; top: 720px; width: 372px; height: 137px; }

  .referral { left: 413px; top: 324px; width: 379px; height: 535px; }
  .form { position: absolute; left: 48px; top: 42px; right: 30px; font-size: 11px; }
  .row { display: flex; align-items: flex-end; gap: 6px; height: 20px; }
  .fill { flex: 1; border-bottom: 1px solid var(--line); height: 12px; }
  .ticks { display: grid; grid-template-columns: 74px 80px; gap: 2px 6px; font-size: 10px; }
  .box { display: inline-block; width: 8px; height: 8px; border: 1px solid var(--line); margin-right: 4px; vertical-align: -1px; }
  .services { list-style: none; margin-top: 18px; font-size: 10.5px; line-height: 17.5px; }
  .refer { position: absolute; left: 48px; top: 325px; right: 40px; font-size: 10.5px; }
  .refer .row { height: 22px; }
  .contact-opts { display: grid; grid-template-columns: 56px 60px; gap: 3px 4px; margin-left: 152px; margin-top: -14px; font-size: 10px; }
</style>
</head>
<body>

<svg class="gradients" aria-hidden="true">
  <defs>
    <linearGradient id="gold" x1="0" y1="0" x2="1" y2="1">
      <stop offset="0" stop-color="#f8d65a"/>
      <stop offset="0.55" stop-color="#f0b52a"/>
      <stop offset="1" stop-color="#e39a17"/>
    </linearGradient>
    <linearGradient id="sky" x1="0" y1="0" x2="0" y2="1">
      <stop offset="0" stop-color="#ffffff"/>
      <stop offset="1" stop-color="#bfe0f0"/>
    </linearGradient>
  </defs>
</svg>

<section class="piece card-back">
  <svg class="art" viewBox="0 0 317 161" preserveAspectRatio="none">
    <path d="M0 128 C90 118 200 150 317 95 L317 161 L0 161 Z" fill="url(#gold)"/>
  </svg>
  <div class="brand brand--md" style="left:20px;top:30px;"><span class="dot"></span><span>Bluegate<br>Physiotherapy</span></div>
  <div class="small" style="left:112px;top:78px;font-size:7px;color:var(--brand)">www.bluegatephysio-example.com.au</div>
  <div class="small" style="left:12px;top:145px;">T 08 9000 1234 · F 08 9000 1235 · M 0400 000 000</div>
</section>

<section class="piece card-front">
  <svg class="art" viewBox="0 0 320 166" preserveAspectRatio="none">
    <rect width="320" height="166" fill="url(#gold)"/>
    <path d="M0 40 C80 30 170 70 210 110 C240 140 280 150 320 150 L320 166 L0 166 Z" fill="#fff"/>
  </svg>
  <div class="name">Tom Ellingsworth</div>
  <div class="title">BSc Physiotherapy / Acupuncturist<br>Cert IV Occupational Health &amp; Safety</div>
  <div class="brand brand--md" style="left:14px;top:66px;"><span class="dot"></span><span>Bluegate<br>Physiotherapy</span></div>
  <div class="small" style="left:14px;top:126px;">Unit 3, 48 Kestrel Lane,<br>Pelican Bay WA 6990</div>
  <div class="small" style="left:14px;top:146px;">T 08 9000 1234 &nbsp; F 08 9000 1235</div>
</section>

<section class="piece magnet">
  <svg class="art" viewBox="0 0 274 146" preserveAspectRatio="none">
    <path d="M0 0 L274 0 L274 34 C200 60 120 50 0 20 Z" fill="#ffffff" opacity=".45"/>
    <path d="M70 146 C150 120 220 110 274 70 L274 146 Z" fill="url(#gold)"/>
  </svg>
  <div class="brand brand--md" style="left:22px;top:36px;"><span class="dot"></span><span>Bluegate<br>Physiotherapy</span></div>
  <div class="small" style="left:22px;top:100px;">T 08 9000 1234<br>Unit 3, 48 Kestrel Lane, Pelican Bay WA 6990<br>www.bluegatephysio-example.com.au</div>
</section>

<section class="piece folder">
  <svg class="art" viewBox="0 0 377 557" preserveAspectRatio="none">
    <path d="M260 0 L377 0 L377 150 C350 70 310 25 260 0 Z" fill="url(#gold)"/>
    <path d="M0 420 C90 350 230 340 377 300 L377 557 L0 557 Z" fill="url(#gold)"/>
    <path d="M0 470 C120 440 260 460 377 440" stroke="#e39a17" stroke-width="1" fill="none" opacity=".6"/>
  </svg>
  <div class="brand brand--lg" style="left:28px;top:212px;"><span class="dot"></span><span>Bluegate<br>Physiotherapy</span></div>
</section>

<section class="piece referral">
  <svg class="art" viewBox="0 0 379 535" preserveAspectRatio="none">
    <path d="M240 0 L379 0 L379 70 C340 25 300 8 240 0 Z" fill="url(#gold)"/>
    <rect x="0" y="300" width="379" height="235" fill="url(#sky)"/>
    <path d="M0 455 C60 470 90 510 110 535 L0 535 Z" fill="url(#gold)"/>
    <path d="M280 535 C320 500 350 490 379 488 L379 535 Z" fill="url(#gold)"/>
  </svg>
  <div class="form">
    <div class="row"><span>Patient Name</span><span class="fill"></span></div>
    <div style="display:flex;gap:10px;margin-top:4px;">
      <div class="row" style="width:130px;"><span>Date</span><span class="fill"></span></div>
      <div class="ticks" style="margin-top:6px;">
        <span><span class="box"></span>W.C.</span><span><span class="box"></span>Vet. Affairs</span>
        <span><span class="box"></span>Private</span><span><span class="box"></span>EPC</span>
      </div>
    </div>
    <ul class="services">
      <li><span class="box"></span>Manual Therapy</li>
      <li><span class="box"></span>Massage</li>
      <li><span class="box"></span>Exercise Prescription</li>
      <li><span class="box"></span>Gym Based Rehab</li>
      <li><span class="box"></span>Workplace Assessment</li>
      <li><span class="box"></span>Ergonomics</li>
      <li><span class="box"></span>Acupuncture</li>
      <li><span class="box"></span>Sports Physiotherapy</li>
      <li><span class="box"></span>Women's Health</li>
    </ul>
  </div>
  <div class="refer">
    <div class="row"><span>Referring Doctor</span><span class="fill"></span></div>
    <div class="row"><span>Sign</span><span class="fill"></span></div>
    <div class="row"><span>Doctor's Name</span><span class="fill"></span></div>
    <div class="row"><span>Address</span><span class="fill"></span></div>
    <div class="row"><span>Preferred method of contact:</span></div>
    <div class="contact-opts">
      <span><span class="box"></span>Email</span><span><span class="box"></span>Phone</span>
      <span><span class="box"></span>Fax</span><span><span class="box"></span>Snail Mail</span>
    </div>
  </div>
  <div class="brand brand--sm" style="left:130px;top:490px;"><span class="dot"></span><span>Bluegate Physiotherapy</span></div>
</section>

<section class="piece letterhead">
  <svg class="art" viewBox="0 0 372 372" preserveAspectRatio="none">
    <path d="M290 0 L372 0 L372 80 C350 35 320 12 290 0 Z" fill="url(#gold)"/>
    <path d="M150 372 C240 335 310 320 372 318 L372 372 Z" fill="url(#gold)"/>
  </svg>
  <div class="brand brand--sm" style="left:236px;top:262px;"><span class="dot"></span><span>Bluegate<br>Physiotherapy</span></div>
  <div class="small" style="left:236px;top:290px;font-size:5.5px;">www.bluegatephysio-example.com.au</div>
</section>

<section class="piece envelope">
  <svg class="art" viewBox="0 0 372 137" preserveAspectRatio="none">
    <path d="M200 137 C270 110 330 100 372 98 L372 137 Z" fill="url(#gold)"/>
  </svg>
  <div class="brand brand--sm" style="left:10px;top:12px;"><span class="dot"></span><span>Bluegate<br>Physiotherapy</span></div>
</section>

</body>
</html>
```